Quenvo Festivals

We need a website that covers a website with reviews about different festivals all around the world. Should include a directory of festivals and artists as well as a nice overview of articles.

Should include
Homepage,
Directory over artists and a detail page for artists also linking them to
a directory over festivals and a detail page for each festival with different information boxes
A nice and clean article category view for possible use of sub categories from main article archive
A modern, clean and good article page

Target Market(s)

People from all over the world that travels to music festivals and enjoys to check information online and share good deals.

Industry/Entity Type

Festival

Requirements
Must have
• Review pages with boxes and spaces for information about festivals

```html
<!DOCTYPE html>
<html lang="en">
<head>
<meta charset="utf-8">
<title>Quenvo Festivals</title>
<link href="https://fonts.googleapis.com/css2?family=Mulish:wght@400;700&family=PT+Sans:wght@400;700&family=Noto+Serif:ital@0;1&display=swap" rel="stylesheet">
<style>
:root{
  --page-dark:#1b1b1b;
  --panel:#e8e8e8;
  --nav:#efefef;
  --nav-line:#c9c9c9;
  --accent:#f39a1e;
  --text:#555555;
  --text-dark:#3c3c3c;
  --rule:#4a4a4a;
  --button:#4a7fa3;
  --white:#ffffff;
  --icon:#444444;
}
*{box-sizing:border-box;margin:0;padding:0}
html,body{width:1200px;height:2228px;overflow:hidden}
body{position:relative;background:var(--page-dark);font-family:"PT Sans",Arial,sans-serif;color:var(--text)}
.abs{position:absolute}
.hero-backdrop{left:0;top:0;width:1200px;height:757px;background:linear-gradient(180deg,#6d6d6d 0%,#9a9a9a 35%,#bdbdbd 60%,#7a7a7a 100%)}
.brand{left:45px;top:44px;display:flex;align-items:center;gap:14px}
.brand-mark{width:52px;height:52px;border-radius:50%;background:var(--accent)}
.brand-name{font-family:"Mulish",sans-serif;font-weight:700;font-size:30px;color:var(--accent);letter-spacing:1px}
.social{left:918px;top:76px;display:flex;gap:9px}
.social span{width:27px;height:27px;border-radius:50%;background:var(--white);border:3px solid #8a8a8a}
.main-nav{left:30px;top:137px;width:1142px;height:63px;background:var(--nav);display:flex;font-size:16px;color:var(--text-dark)}
.main-nav a{color:inherit;text-decoration:none;height:63px;line-height:63px;border-right:1px solid var(--nav-line);white-space:nowrap}
.panel{left:30px;top:226px;width:1142px;height:1895px;background:var(--panel)}
.slide{left:65px;top:261px;width:1071px;height:474px;background:linear-gradient(180deg,#6f8a5a 0%,#5f8a3e 55%,#4e7a33 100%)}
.caption{left:77px;top:688px;width:532px;height:35px;background:rgba(255,255,255,.9);font-size:15px;line-height:35px;padding-left:18px;color:#333;white-space:nowrap}
.slider-nav{left:510px;top:749px;display:flex;align-items:center;gap:6px}
.slider-nav .arrow{width:30px;height:30px;border-radius:50%;background:#555;color:#fff;font-size:16px;line-height:28px;text-align:center}
.slider-nav .dot{width:14px;height:14px;border-radius:50%;background:#4a4a4a}
.slider-nav .dot.on{background:transparent;border:2px solid #4a4a4a}
.intro{left:90px;top:806px;width:1022px;text-align:center;font-family:"Noto Serif",serif;font-style:italic;font-size:22px;line-height:37px;color:var(--text-dark)}
.double-rule{left:65px;width:1071px;height:8px;border-top:3px solid var(--rule);border-bottom:1px solid var(--rule)}
.rule{left:65px;width:1071px;border-top:1px solid var(--rule)}
.heading{font-family:"Mulish",sans-serif;font-weight:400;font-size:22px;color:var(--accent)}
.body-copy{font-size:15px;line-height:24px}
.feature-list{left:802px;top:1017px;list-style:none;font-family:"Noto Serif",serif;font-style:italic;font-size:14px;line-height:24px;color:var(--text-dark)}
.feature-list li::before{content:"›";font-style:normal;margin-right:12px}
.service{width:230px;text-align:center;top:1160px}
.service svg{display:block;margin:0 auto}
.service h3{font-family:"Mulish",sans-serif;font-weight:400;font-size:20px;color:var(--accent);margin:20px 0 14px}
.service p{font-size:15px;line-height:24px}
.work-arrows{left:1078px;top:1431px;display:flex;gap:8px}
.work-arrows span{width:26px;height:26px;border-radius:50%;background:#555;color:#fff;font-size:14px;line-height:25px;text-align:center}
.work-thumb{top:1480px;width:196px;height:155px}
.post{left:65px;width:235px;height:73px;border-bottom:1px dashed #8a8a8a;display:flex;gap:14px;padding-top:8px}
.post-date{width:36px;text-align:center;font-family:"Noto Serif",serif;color:var(--text-dark)}
.post-date b{display:block;font-weight:400;font-size:26px;line-height:26px}
.post-date i{font-size:12px;text-transform:uppercase}
.post p{font-size:15px;line-height:24px;white-space:nowrap}
.snap{width:70px;height:70px}
.field{left:900px;width:180px;height:37px;background:var(--white);border:1px solid #cfcfcf;border-radius:3px}
.field-label{left:1090px;font-size:13px;color:var(--text-dark)}
.submit{left:900px;top:2052px;width:100px;height:32px;background:var(--button);color:#fff;border-radius:2px;font-family:"Noto Serif",serif;font-style:italic;font-size:15px;line-height:32px;text-align:center}
.site-footer{left:30px;top:2144px;width:1142px;height:60px;background:var(--panel);text-align:center;font-size:13px;line-height:60px;color:var(--text-dark)}
</style>
</head>
<body>
<div class="abs hero-backdrop" role="img" aria-label="Black and white photo of a covered city shopping arcade"></div>

<header>
  <div class="abs brand"><span class="brand-mark"></span><span class="brand-name">Quenvo Festivals</span></div>
  <div class="abs social" aria-label="Social links"><span></span><span></span><span></span><span></span><span></span><span></span><span></span></div>
  <nav class="abs main-nav">
    <a style="width:120px;padding-left:35px">Home</a>
    <a style="width:141px;padding-left:32px">Festivals</a>
    <a style="width:109px;padding-left:30px">Artists</a>
    <a style="width:117px;padding-left:30px">Reviews</a>
    <a style="width:118px;padding-left:30px">Articles</a>
    <a style="width:136px;padding-left:37px">Contact</a>
  </nav>
</header>

<main>
  <div class="abs panel"></div>

  <div class="abs slide" role="img" aria-label="Festival crowd on a lawn with children in a sack race and a performer in a colourful costume"></div>
  <div class="abs caption">Review: a sunny weekend of street bands, games and parades.</div>
  <div class="abs slider-nav"><span class="arrow">‹</span><span class="dot"></span><span class="dot"></span><span class="dot"></span><span class="dot"></span><span class="dot on"></span><span class="arrow">›</span></div>

  <p class="abs intro">Honest reviews of music festivals all around the world, with line-ups, camping, travel tips and the best ticket deals shared by fellow festival fans.</p>

  <div class="abs double-rule" style="top:922px"></div>

  <h2 class="abs heading" style="left:65px;top:973px">What We Cover</h2>
  <p class="abs body-copy" style="left:65px;top:1013px;width:690px">Quenvo Festivals reviews music festivals on every continent, from small village weekends to giant city stages. Each review rates the line-up, sound, camping, food, travel and value, with info boxes for dates, prices and capacity. Browse the festival directory, find the artists you love and see where they play next, then share your own tips and deals.</p>
  <ul class="abs feature-list">
    <li>Festival reviews with rating boxes.</li>
    <li>Directory of festivals worldwide.</li>
    <li>Artist pages linked to their festivals.</li>
    <li>Articles, guides and ticket deals.</li>
  </ul>

  <div class="abs service" style="left:66px">
    <svg width="56" height="50" viewBox="0 0 56 50"><path d="M28 3 L34 18 L50 19 L38 30 L42 46 L28 37 L14 46 L18 30 L6 19 L22 18 Z" fill="var(--icon)"/></svg>
    <h3>Festival Reviews</h3>
    <p>Ratings for line-up, sound, camping, food and value at every festival.</p>
  </div>
  <div class="abs service" style="left:345px">
    <svg width="56" height="50" viewBox="0 0 56 50"><rect x="21" y="3" width="14" height="24" rx="7" fill="var(--icon)"/><path d="M14 22 A14 14 0 0 0 42 22" fill="none" stroke="var(--icon)" stroke-width="3"/><rect x="26" y="36" width="4" height="8" fill="var(--icon)"/><rect x="18" y="44" width="20" height="4" fill="var(--icon)"/></svg>
    <h3>Artist Directory</h3>
    <p>Find your favourite artists and the festivals where they play next.</p>
  </div>
  <div class="abs service" style="left:625px">
    <svg width="56" height="50" viewBox="0 0 56 50"><path d="M28 48 C16 32 12 26 12 18 A16 16 0 0 1 44 18 C44 26 40 32 28 48 Z" fill="var(--icon)"/><circle cx="28" cy="18" r="6" fill="#e8e8e8"/></svg>
    <h3>Festival Directory</h3>
    <p>Dates, locations, prices and info boxes for festivals around the world.</p>
  </div>
  <div class="abs service" style="left:902px">
    <svg width="56" height="50" viewBox="0 0 56 50"><path d="M4 6 H28 L52 30 L32 48 L4 20 Z" fill="var(--icon)"/><circle cx="15" cy="16" r="4" fill="#e8e8e8"/></svg>
    <h3>Ticket Deals</h3>
    <p>Travellers share the best ticket, travel and camping deals they find.</p>
  </div>

  <div class="abs rule" style="top:1387px"></div>

  <h2 class="abs heading" style="left:65px;top:1430px">Latest Reviews</h2>
  <div class="abs work-arrows"><span>‹</span><span>›</span></div>
  <div class="abs work-thumb" style="left:65px;background:linear-gradient(180deg,#8a8f95,#b24a3a)" role="img" aria-label="Street parade of dancers in red costumes"></div>
  <div class="abs work-thumb" style="left:284px;background:linear-gradient(180deg,#7b5a8a,#d8b23a)" role="img" aria-label="Festival float with performers in yellow"></div>
  <div class="abs work-thumb" style="left:503px;background:linear-gradient(180deg,#c9c2b8,#8a3a3a)" role="img" aria-label="Street festival procession under bunting"></div>
  <div class="abs work-thumb" style="left:722px;background:linear-gradient(180deg,#4a7a5a,#3a5aa8)" role="img" aria-label="Colourful costumed dancers at a festival"></div>
  <div class="abs work-thumb" style="left:940px;background:linear-gradient(180deg,#b9a34a,#a83a2a)" role="img" aria-label="Festival stage with performers in red and gold"></div>

  <div class="abs double-rule" style="top:1682px"></div>

  <h2 class="abs heading" style="left:65px;top:1736px">Latest Articles</h2>
  <div class="abs post" style="top:1774px"><div class="post-date"><b>22</b><i>Jun</i></div><p>Ten camping tips for<br>first-time festivals</p></div>
  <div class="abs post" style="top:1847px"><div class="post-date"><b>14</b><i>May</i></div><p>Summer line-ups we<br>cannot wait to see</p></div>
  <div class="abs post" style="top:1920px"><div class="post-date"><b>11</b><i>May</i></div><p>Budget travel to big<br>European festivals</p></div>
  <div class="abs post" style="top:1993px;border-bottom:none"><div class="post-date"><b>08</b><i>Apr</i></div><p>Street carnivals worth<br>a long trip abroad</p></div>

  <h2 class="abs heading" style="left:343px;top:1736px">Snapshots</h2>
  <div class="abs snap" style="left:343px;top:1782px;background:linear-gradient(#d8cfc0,#8a9a5a)" role="img" aria-label="Festival snapshot"></div>
  <div class="abs snap" style="left:428px;top:1782px;background:linear-gradient(#e8e2d6,#b59a6a)" role="img" aria-label="Festival snapshot"></div>
  <div class="abs snap" style="left:511px;top:1782px;background:linear-gradient(#e6dcd6,#c9aa9a)" role="img" aria-label="Festival snapshot"></div>
  <div class="abs snap" style="left:343px;top:1865px;background:linear-gradient(#e6d6cc,#c9957a)" role="img" aria-label="Festival snapshot"></div>
  <div class="abs snap" style="left:428px;top:1865px;background:linear-gradient(#c9b89a,#8a7a5a)" role="img" aria-label="Festival snapshot"></div>
  <div class="abs snap" style="left:511px;top:1865px;background:linear-gradient(#eeeeee,#6a9a4a)" role="img" aria-label="Festival snapshot"></div>
  <div class="abs snap" style="left:343px;top:1950px;background:linear-gradient(#e6e2dc,#b57a5a)" role="img" aria-label="Festival snapshot"></div>
  <div class="abs snap" style="left:428px;top:1950px;background:linear-gradient(#cfe0ee,#3a7ab5)" role="img" aria-label="Festival snapshot"></div>
  <div class="abs snap" style="left:511px;top:1950px;background:linear-gradient(#eeeeee,#c9c2b8)" role="img" aria-label="Festival snapshot"></div>

  <h2 class="abs heading" style="left:622px;top:1736px">About</h2>
  <p class="abs body-copy" style="left:622px;top:1780px;width:232px">Quenvo Festivals is written by fans who travel the world for live music. We visit each festival, rate what matters and keep a growing directory of events and artists.</p>
  <p class="abs body-copy" style="left:622px;top:1958px;width:232px">Been somewhere great? Send us your review or a deal to share.</p>

  <h2 class="abs heading" style="left:900px;top:1736px">Get in Touch</h2>
  <div class="abs field" style="top:1782px"></div><span class="abs field-label" style="top:1792px">Name*</span>
  <div class="abs field" style="top:1832px"></div><span class="abs field-label" style="top:1842px">Email*</span>
  <div class="abs field" style="top:1883px;width:233px;height:155px"></div>
  <div class="abs submit">Submit</div>
</main>

<footer class="abs site-footer">© 2011 Northlane Studio. All Right Reserved.</footer>
</body>
</html>
```